Pemberton Dialworks Business Card Design

Double Sided Business Card Design for a Locksmith company specializing in Safecracking, safe & vault service.

```html
<!DOCTYPE html>
<html lang="en">
<head>
<meta charset="utf-8">
<title>Pemberton Dialworks — Business Card</title>
<link href="https://fonts.googleapis.com/css2?family=Oswald:wght@300;500;600&family=Saira+Condensed:wght@500&display=swap" rel="stylesheet">
<style>
  :root {
    --bg-top: #262626;
    --bg-bottom: #050505;
    --green: #3b8a44;
    --green-glow: #4fbf5c;
    --white: #f4f4f4;
  }
  * { margin: 0; padding: 0; box-sizing: border-box; }
  html, body { width: 1200px; height: 686px; overflow: hidden; background: #000; }
  .card {
    position: relative;
    width: 1200px;
    height: 686px;
    overflow: hidden;
    background: linear-gradient(180deg, var(--bg-top) 0%, #111 55%, var(--bg-bottom) 100%);
  }
  .card__divider {
    position: absolute;
    left: 589px;
    top: 0;
    width: 8px;
    height: 686px;
    background: linear-gradient(90deg, #0a0a0a 0%, var(--green) 40%, var(--green-glow) 50%, var(--green) 60%, #0a0a0a 100%);
    box-shadow: 0 0 10px rgba(79, 191, 92, 0.35);
  }
  .brand {
    position: absolute;
    right: 680px;
    top: 205px;
    display: flex;
    align-items: center;
    gap: 18px;
  }
  .brand__mark {
    width: 62px;
    height: 62px;
    border-radius: 50%;
    background: var(--green);
  }
  .brand__name {
    font-family: 'Oswald', sans-serif;
    font-weight: 600;
    font-size: 38px;
    line-height: 1.02;
    letter-spacing: 1px;
    color: var(--green);
    text-transform: uppercase;
  }
  .person {
    position: absolute;
    right: 680px;
    top: 325px;
    text-align: right;
  }
  .person__name {
    font-family: 'Oswald', sans-serif;
    font-weight: 600;
    font-size: 84px;
    line-height: 1;
    color: var(--green);
    letter-spacing: 0.5px;
  }
  .person__name-last { font-weight: 300; }
  .person__role {
    margin-top: 4px;
    font-family: 'Oswald', sans-serif;
    font-weight: 500;
    font-size: 32px;
    line-height: 1.1;
    color: var(--white);
  }
  .contacts {
    position: absolute;
    left: 654px;
    top: 159px;
    list-style: none;
  }
  .contact {
    display: flex;
    align-items: center;
    height: 78px;
    margin-bottom: 27px;
  }
  .contact__icon {
    width: 78px;
    height: 78px;
    border: 3px solid var(--green);
    border-radius: 50%;
    display: flex;
    align-items: center;
    justify-content: center;
    flex-shrink: 0;
  }
  .contact__icon svg { width: 38px; height: 38px; fill: var(--green); }
  .contact__text {
    margin-left: 23px;
    font-family: 'Saira Condensed', sans-serif;
    font-weight: 500;
    font-size: 31px;
    color: var(--white);
    white-space: nowrap;
  }
</style>
</head>
<body>
<div class="card">
  <div class="card__divider"></div>

  <div class="brand">
    <div class="brand__mark"></div>
    <div class="brand__name">Pemberton<br>Dialworks</div>
  </div>

  <div class="person">
    <div class="person__name">JOHN MARK <span class="person__name-last">DOE</span></div>
    <div class="person__role">PROJECT MANAGER</div>
  </div>

  <ul class="contacts">
    <li class="contact">
      <span class="contact__icon">
        <svg viewBox="0 0 24 24"><path d="M12 2a7 7 0 0 0-7 7c0 5.2 7 13 7 13s7-7.8 7-13a7 7 0 0 0-7-7zm0 9.6A2.6 2.6 0 1 1 12 6.4a2.6 2.6 0 0 1 0 5.2z"/></svg>
      </span>
      <span class="contact__text">Street No. Building No. City. State</span>
    </li>
    <li class="contact">
      <span class="contact__icon">
        <svg viewBox="0 0 24 24"><path d="M6.6 2.5 9.3 2l1.6 4.6-2 1.5c.9 2.6 2.6 4.7 4.9 6.2l1.8-1.7 4.4 2-.5 2.8c-.2 1-1.1 1.7-2.1 1.6C9.6 18.4 4.6 12.6 4.8 4.6c0-1 .8-1.9 1.8-2.1z"/></svg>
      </span>
      <span class="contact__text">000-000-0000</span>
    </li>
    <li class="contact">
      <span class="contact__icon">
        <svg viewBox="0 0 24 24" fill="none" stroke="#3b8a44" stroke-width="1.6" style="fill:none"><circle cx="12" cy="12" r="9"/><ellipse cx="12" cy="12" rx="4" ry="9"/><path d="M3 12h18M4.5 7.5h15M4.5 16.5h15M12 3v18"/></svg>
      </span>
      <span class="contact__text">www.website.com</span>
    </li>
    <li class="contact">
      <span class="contact__icon">
        <svg viewBox="0 0 24 24"><path d="M2 5h20v14H2z"/><path d="M2 5l10 8 10-8" fill="none" stroke="#0d0d0d" stroke-width="1.6"/><path d="M2 19l8-7M22 19l-8-7" fill="none" stroke="#0d0d0d" stroke-width="1.4"/></svg>
      </span>
      <span class="contact__text">email@info.com</span>
    </li>
  </ul>
</div>
</body>
</html>
```